US company marketing to law enforcement needs brochure design

We have created a new logo and now need to update our printed material. What we really need is a "style" or "template" for how our brochures will look in the future. Enclosed is the brochure draft with the old style and logo. Also enclosed is the new logo. As we are marketing to US law enforcement it is important the the brochure design is strong, powerful and that we are looking experienced and trustworthy. However, we also want to look modern in line with the logo update.

Target Market(s)

Law enforcement

Industry/Entity Type

Marketing

```html
<!DOCTYPE html>
<html lang="en">
<head>
<meta charset="utf-8">
<title>Steadfast Services – Brochure Cover</title>
<link rel="stylesheet" href="https://fonts.googleapis.com/css2?family=Source+Sans+3:wght@400;600&display=swap">
<style>
  :root {
    --navy: #1e3768;
    --navy-soft: #334c7e;
    --slate: #5f7296;
    --name-grey: #8c8c8c;
    --white: #ffffff;
    --paper: #f4f2ef;
  }
  * { margin: 0; padding: 0; box-sizing: border-box; }
  html, body {
    width: 1200px;
    height: 849px;
    overflow: hidden;
    background: var(--paper);
  }
  .cover-spread {
    position: relative;
    width: 1200px;
    height: 847px;
    margin-top: 1px;
    font-family: "Source Sans 3", "Helvetica Neue", Arial, sans-serif;
  }
  .cover-shapes {
    position: absolute;
    inset: 0;
    width: 1200px;
    height: 847px;
    display: block;
  }
  .brand {
    position: absolute;
    left: 681px;
    top: 45px;
    height: 74px;
    display: flex;
    align-items: center;
    gap: 20px;
  }
  .brand-dot {
    width: 74px;
    height: 74px;
    border-radius: 50%;
    background: var(--navy);
  }
  .brand-name {
    font-size: 38px;
    font-weight: 600;
    color: var(--name-grey);
    letter-spacing: -0.3px;
  }
  .service-list {
    position: absolute;
    left: 600px;
    width: 600px;
    list-style: none;
    display: flex;
    justify-content: center;
    align-items: center;
    color: var(--white);
    font-size: 19.5px;
    font-weight: 400;
    gap: 0;
  }
  .service-list.row-one { top: 727px; left: 598px; }
  .service-list.row-two { top: 773px; left: 596px; }
  .service-list li + li::before {
    content: "";
    display: inline-block;
    width: 7px;
    height: 7px;
    border-radius: 50%;
    background: var(--white);
    margin: 0 23px 0 25px;
    vertical-align: middle;
    position: relative;
    top: -2px;
  }
</style>
</head>
<body>
  <main class="cover-spread">
    <svg class="cover-shapes" viewBox="0 0 1368 966" preserveAspectRatio="none" xmlns="http://www.w3.org/2000/svg">
      <defs>
        <linearGradient id="photo-tones" x1="0" y1="0" x2="0.35" y2="1">
          <stop offset="0" stop-color="#f6e6d3"/>
          <stop offset="0.35" stop-color="#e8c9a6"/>
          <stop offset="0.6" stop-color="#b78a62"/>
          <stop offset="0.85" stop-color="#5a2c22"/>
          <stop offset="1" stop-color="#2e1714"/>
        </linearGradient>
      </defs>

      <!-- back panel -->
      <rect class="back-panel" x="0" y="0" width="684" height="966" fill="var(--navy)"/>
      <circle class="back-emblem-disc" cx="342" cy="396" r="182" fill="var(--navy-soft)"/>
      <path class="back-lower-band" d="M0,633 C60,780 200,870 380,868 C500,866 620,835 684,800 L684,966 L0,966 Z" fill="var(--slate)"/>

      <!-- front panel photo area -->
      <rect class="front-photo" x="684" y="0" width="684" height="966" fill="url(#photo-tones)" role="img" aria-label="Photo of a wooden judge's gavel with a brass band resting on its block before an open law book"/>
      <path class="front-lower-band" d="M684,786 C880,725 1120,640 1368,748 L1368,966 L684,966 Z" fill="var(--navy)"/>

      <!-- sweeping accent line -->
      <path class="accent-swoosh" d="M89,853 C200,922 420,920 684,836 C900,766 1150,648 1350,672 C1150,662 900,760 684,824 C440,900 220,906 89,853 Z" fill="var(--navy)"/>
    </svg>

    <div class="brand">
      <span class="brand-dot"></span>
      <span class="brand-name">SteadfastServices</span>
    </div>

    <ul class="service-list row-one">
      <li>Pre Trial</li>
      <li>Diversion</li>
      <li>Deferred Prosecution</li>
    </ul>
    <ul class="service-list row-two">
      <li>Jail Alternative</li>
      <li>Probation</li>
    </ul>
  </main>
</body>
</html>
```